Fenwick Hollow at Cedar Basin Marketing Sign

I need a sign designed that will be 4'X8'. You designed another sign for me not too long ago - Stonecrest at Marlow's Point. I need another sign similar in layout, but with the Fenwick Hollow logo, tagline, rendering, colors, etc.

Attached is the logo, and rendering. Here are the other items I need to have on this sign:
Tagline - Life Outside The Lines
JOIN OUR WAITLIST TODAY!
Move-In Beginning Summer 2017
www.fenwickhollowliving.example

```html
<!DOCTYPE html>
<html lang="en">
<head>
<meta charset="utf-8">
<title>Fenwick Hollow at Cedar Basin – Marketing Sign</title>
<link rel="stylesheet" href="https://fonts.googleapis.com/css2?family=Signika:wght@400;600&family=Oswald:wght@700&family=Roboto+Condensed:wght@700&family=Open+Sans:wght@400&display=swap">
<style>
  :root {
    --page-bg: #eef1f4;
    --navy: #0f3a64;
    --navy-deep: #0a2c4f;
    --teal: #1b86b0;
    --teal-light: #2aa3c9;
    --accent-blue: #1f6fc0;
    --silver-top: #f4f5f6;
    --silver-bottom: #b9bcbf;
    --brand-teal: #1d93bd;
    --headline-light: #f1f2f3;
    --headline-shade: #b8bec4;
    --white: #ffffff;
  }
  * { margin: 0; padding: 0; box-sizing: border-box; }
  html, body {
    width: 1200px; height: 908px; overflow: hidden;
    background: var(--page-bg);
  }
  .sign {
    position: absolute; left: 40px; top: 174px;
    width: 1120px; height: 560px;
    overflow: hidden;
    box-shadow: 0 6px 24px rgba(0,0,0,.18);
    background: var(--navy);
  }
  .sign-shapes { position: absolute; inset: 0; }
  .brand {
    position: absolute; left: 640px; width: 420px; top: 36px;
    display: flex; flex-direction: column; align-items: center;
    font-family: "Signika", sans-serif; font-weight: 400;
    color: var(--brand-teal);
  }
  .brand-mark {
    width: 62px; height: 62px;
    background: var(--brand-teal);
    margin-bottom: 12px;
  }
  .brand-name { font-size: 30px; line-height: 1; letter-spacing: .5px; }
  .brand-place { font-size: 15px; line-height: 1.3; }
  .tagline {
    position: absolute; left: 654px; top: 224px;
    width: 396px; height: 58px;
    border: 1.5px solid rgba(255,255,255,.75);
    display: flex; align-items: center; justify-content: center;
    font-family: "Signika", sans-serif; font-weight: 600;
    font-size: 32px; color: var(--white);
  }
  .headline {
    position: absolute; left: 610px; width: 480px; top: 300px;
    text-align: center;
    font-family: "Oswald", sans-serif; font-weight: 700;
    font-size: 56px; line-height: 70px;
    color: var(--headline-light);
    background: linear-gradient(var(--headline-light) 40%, var(--headline-shade));
    -webkit-background-clip: text; background-clip: text;
    -webkit-text-fill-color: transparent;
    filter: drop-shadow(2px 2px 0 rgba(0,0,0,.35));
  }
  .move-in {
    position: absolute; left: 610px; width: 480px; top: 472px;
    text-align: center;
    font-family: "Roboto Condensed", sans-serif; font-weight: 700;
    font-size: 32px; color: var(--white);
  }
  .website {
    position: absolute; left: 610px; width: 480px; top: 522px;
    display: flex; align-items: center; justify-content: center; gap: 6px;
    font-family: "Open Sans", sans-serif; font-size: 15px;
    color: rgba(255,255,255,.9);
  }
  .website-dot { width: 7px; height: 7px; border-radius: 50%; background: rgba(255,255,255,.8); }
</style>
</head>
<body>
  <div class="sign">
    <svg class="sign-shapes" width="1120" height="560" viewBox="0 0 1120 560">
      <defs>
        <linearGradient id="silverPanel" x1="0" y1="0" x2="0" y2="1">
          <stop offset="0" stop-color="var(--silver-top)"/>
          <stop offset="1" stop-color="var(--silver-bottom)"/>
        </linearGradient>
        <linearGradient id="tealBand" x1="0" y1="0" x2="1" y2="0">
          <stop offset="0" stop-color="var(--teal-light)"/>
          <stop offset="1" stop-color="var(--teal)"/>
        </linearGradient>
        <linearGradient id="renderingTone" x1="0" y1="0" x2="0" y2="1">
          <stop offset="0" stop-color="#c9dbe8"/>
          <stop offset=".35" stop-color="#b8c49a"/>
          <stop offset=".6" stop-color="#c9b79a"/>
          <stop offset=".8" stop-color="#8a7f7a"/>
          <stop offset="1" stop-color="#7f9a6a"/>
        </linearGradient>
      </defs>
      <!-- right panels -->
      <rect class="silver-panel" x="0" y="0" width="1120" height="195" fill="url(#silverPanel)"/>
      <rect class="navy-panel" x="0" y="195" width="1120" height="260" fill="var(--navy)"/>
      <rect class="teal-band" x="0" y="455" width="1120" height="105" fill="url(#tealBand)"/>
      <!-- chevron stripe -->
      <polygon class="chevron-stripe" points="480,0 506,0 592,195 431,560 405,560 566,195" fill="var(--accent-blue)"/>
      <polygon class="chevron-edge" points="506,0 518,0 604,195 443,560 431,560 592,195" fill="var(--navy-deep)"/>
      <!-- rendering area -->
      <polygon class="rendering" role="img" aria-label="Watercolour rendering of the three-storey apartment buildings with trees, parking and landscaping"
        points="0,0 480,0 566,195 405,560 0,560" fill="url(#renderingTone)"/>
    </svg>

    <div class="brand">
      <div class="brand-mark"></div>
      <div class="brand-name">Fenwick Hollow</div>
      <div class="brand-place">at Cedar Basin</div>
    </div>

    <div class="tagline">Life Outside The Lines</div>
    <div class="headline">JOIN OUR WAITLIST<br>TODAY!</div>
    <div class="move-in">Move-In Beginning Summer 2017</div>
    <div class="website"><span class="website-dot"></span>www.fenwickhollowliving.example</div>
  </div>
</body>
</html>
```